Membership card Design

Hi I need a new membership card design for a social University club located in New Zealand. Our club name is called Maple Crest Society (MCSOC) and we provide a social hub for international students from Asia to meet local students. We are a non-profit organization that organizes activities such as paintball, ski trips, parties and day trips for our members. We need designs that look more like a membership card than a name card because we will be giving them to our members as a proof of membership. We would prefer a design that is simple in the front and with our club details, contacts and a place to write down a membership number on the back. We would like our card to have designs using the colours red, black, grey and orange. The design must incoporate the logo attached in this project. If possible, we would like the flower in the Hong Kong Flag to be incoporated in the design. The final design must look more like a membership card than a name card and communicate professionalism and high quality.

Target Market(s)

University Students

Industry/Entity Type

Non-Profit

Requirements
Must have
• The design must include:

The logo of our club
Our facebook page details: www.friendspage.example/maplecrest.soc
Our email: maplecrestsoc@mailbox.example
A place behind the card to print membership numbers.

```html
<!DOCTYPE html>
<html lang="en">
<head>
<meta charset="utf-8">
<title>Maple Crest Society – Membership Card</title>
<link href="https://fonts.googleapis.com/css2?family=Cinzel:wght@400;700&display=swap" rel="stylesheet">
<style>
  :root {
    --bg: #3a3836;
    --card-black: #0b0b0b;
    --orange-light: #c9801e;
    --orange-mid: #8f4f10;
    --orange-dark: #3b1d06;
    --crest-red: #a3200f;
    --crest-brown: #4a2308;
    --number-ink: #3d0905;
    --red: #c4161c;
    --white: #f2f2f2;
    --grey: #9a9a9a;
  }
  * { margin: 0; padding: 0; box-sizing: border-box; }
  html, body { width: 1200px; height: 718px; overflow: hidden; background: var(--bg); }
  .canvas { position: relative; width: 1200px; height: 718px; }

  .card {
    position: absolute;
    width: 520px;
    height: 297px;
    border-radius: 3px;
    overflow: hidden;
    box-shadow: 0 8px 22px rgba(0,0,0,.45);
    font-family: "Cinzel", serif;
  }

  /* Back of card */
  .card-back {
    left: 50px;
    top: 80px;
    background: radial-gradient(ellipse at 55% 40%, var(--orange-light) 0%, var(--orange-mid) 55%, var(--orange-dark) 100%);
  }
  .card-back .crest-area {
    position: absolute;
    left: 140px;
    top: 14px;
    width: 250px;
    height: 262px;
    border-radius: 46% 46% 40% 40%;
    background: radial-gradient(circle at 48% 48%, var(--crest-red) 0%, var(--orange-mid) 45%, var(--crest-brown) 100%);
    border: 2px solid rgba(60,25,5,.55);
    opacity: .9;
  }
  .card-back .member-number {
    position: absolute;
    left: 70px;
    bottom: 26px;
    font-size: 21px;
    font-weight: 700;
    letter-spacing: 2px;
    color: var(--number-ink);
  }

  /* Front of card */
  .card-front {
    left: 630px;
    top: 330px;
    background: var(--card-black);
  }
  .card-front .ornament {
    position: absolute;
    left: 0;
    top: 0;
    width: 190px;
    height: 297px;
    background: radial-gradient(ellipse at 20% 40%, rgba(90,30,25,.35) 0%, rgba(40,20,18,.2) 45%, rgba(0,0,0,0) 75%);
  }
  .card-front .brand {
    position: absolute;
    left: 0;
    right: 0;
    top: 88px;
    display: flex;
    align-items: center;
    justify-content: center;
    gap: 12px;
  }
  .card-front .brand-dot {
    width: 18px;
    height: 18px;
    border-radius: 50%;
    background: var(--red);
  }
  .card-front .brand-name {
    font-size: 40px;
    font-weight: 400;
    color: var(--red);
    letter-spacing: 1px;
    white-space: nowrap;
  }
  .card-front .card-title {
    position: absolute;
    left: 0;
    right: 0;
    top: 170px;
    text-align: center;
    font-size: 27px;
    font-weight: 400;
    color: var(--white);
    letter-spacing: 1px;
  }
  .card-front .contacts {
    position: absolute;
    left: 24px;
    right: 18px;
    bottom: 22px;
    display: flex;
    justify-content: space-between;
    font-size: 10px;
    color: var(--white);
    text-transform: uppercase;
    white-space: nowrap;
  }
</style>
</head>
<body>
<main class="canvas">
  <section class="card card-back" aria-label="Membership card back">
    <div class="crest-area" role="img" aria-label="Club crest illustration in orange and red tones"></div>
    <p class="member-number">No. XXX - XXX - XXX - XXX</p>
  </section>

  <section class="card card-front" aria-label="Membership card front">
    <div class="ornament" role="img" aria-label="Faint floral pattern"></div>
    <div class="brand">
      <span class="brand-dot"></span>
      <span class="brand-name">Maple Crest Soc</span>
    </div>
    <h1 class="card-title">Membership Card</h1>
    <div class="contacts">
      <span class="contact-web">www.friendspage.example/maplecrest.soc</span>
      <span class="contact-email">maplecrestsoc@mailbox.example</span>
    </div>
  </section>
</main>
</body>
</html>
```